Mobile App Flyer for Takeaway Tapforge

We need a single A4 page flyer to promote our mobile apps for takeaway food solution.

Please visit our web site www.tapforge-demo.net and review the retail page for further details but here are a number of the benefits that I'd like to try to include in the flyer.

I do need a catchy title too...

TAKEAWAYS & RESTAURANTS
Tap into the growth market of mobile and online food ordering. With over 51% of UK online ecommerce sales now being conducted on mobiles devices* it’s crucial takeaways and restaurants adopt a suitable mobile strategy.
* Source: QWLT / Norvelia 2016
Stay independent. Go mobile with an online food ordering app that is dedicated and designed specifically for your business. Unlike other solutions, we don’t encourage your customer to use a shared app that then promotes your competitors’ businesses to your customers!
We don’t charge order commission, just a small fixed monthly fee, (pricing published on our web site). As you grow your mobile business you keep all the profits!
Benefit from better Brisko search results. Did you know Brisko now favours and ranks businesses with mobile apps higher than those without?
Differentiate your business against other local businesses, create a buzz around your business going “Mobile”!
Free-up your business phone line at peak periods, never miss another order.
Save staff time by accepting unlimited mobile and on-line orders simultaneously, no need to take a call and write the orders down, it also minimises mistakes.
If you buy our Business or Business Plus package we will also provide you an online shop that can be added to your website!
If you’re thinking this isn’t going to be cheap, check our pricing on our web site, you’re going to be very pleasantly surprised.
Attractive interactive menus, show-off your business and food to its best.
Convenience for your customers:
No more holding or busy signal when trying to place an order.
Customer’s order history is saved in the app making re-ordering fast and convenient.
Customers can use convenient online payment providers such as MONEVO, as well as traditional credit cards or of course, cash-on-collection.
Easily and quickly update your menu with seasonal changes, menu items, pricing and even delivery options.
Send promotions to your customers and advise them of seasonal opening times, even message them each time they are close to your business!
Launch an in-app loyalty programme, which rewards your loyal customers and generates repeat business.
There are many reason you should be considering going mobile if. Please call us on 01632 960417 or email us at Info@Tapforge-demo.net to discuss your requirements with us.

Target Market(s)

Owners of takeaways and restaurants

Font styles to use
Sans Serif

Colors
33b8a4
3176b5
faa54b

Requirements
Must have
• Tap forge white and blue logo from website
• Features doc has some screen shots that could be used.
• The format must be reusable for other products so if I develop an app for a golf course, for example, I could use the same layout but change the primary colour of the flyer.
• Doesn't have to be identical to web site but shouldn't be poles apart so that it looks odd!
Nice to have
• At least one picture of a smart phone.

```html
<!DOCTYPE html>
<html lang="en">
<head>
<meta charset="utf-8">
<title>Tapforge – Mobile App Flyer</title>
<link rel="stylesheet" href="https://fonts.googleapis.com/css2?family=Open+Sans:ital,wght@0,800;1,700;1,800&display=swap">
<style>
  :root {
    --brand-blue: #1f72b6;
    --brand-green: #4db590;
    --brand-orange: #f5a84c;
    --orange-shade: #c7782a;
    --paper: #ffffff;
  }
  html, body {
    margin: 0;
    padding: 0;
    width: 858px;
    height: 1200px;
    overflow: hidden;
    background: var(--paper);
  }
  .flyer {
    display: block;
    width: 858px;
    height: 1200px;
    font-family: "Open Sans", Arial, sans-serif;
  }
  .paper { fill: var(--paper); }
  .field { fill: var(--brand-green); }
  .footer-band { fill: var(--brand-orange); }
  .brand-square { fill: var(--brand-blue); }
  .brand-name {
    fill: var(--brand-blue);
    font-weight: 800;
    font-style: normal;
    font-size: 96px;
    letter-spacing: -2px;
  }
  .feature-ribbon { fill: var(--brand-blue); }
  .feature-label {
    fill: var(--paper);
    font-weight: 800;
    font-style: italic;
    font-size: 45px;
  }
  .callout { fill: var(--brand-orange); }
  .callout-text {
    fill: var(--paper);
    font-weight: 700;
    font-style: italic;
    font-size: 20.5px;
  }
  .cta-tab { fill: var(--brand-orange); }
  .cta-fold { fill: var(--orange-shade); }
  .cta-url-bar { fill: var(--paper); }
  .cta-text {
    fill: var(--paper);
    font-weight: 800;
    font-style: italic;
    font-size: 44px;
  }
  .cta-url {
    fill: var(--brand-blue);
    font-weight: 800;
    font-style: italic;
    font-size: 38px;
  }
</style>
</head>
<body>
<svg class="flyer" viewBox="0 0 858 1200" xmlns="http://www.w3.org/2000/svg">
  <defs>
    <linearGradient id="deviceTone" x1="0" y1="0" x2="0" y2="1">
      <stop offset="0" stop-color="#2b2b2b"/>
      <stop offset="0.25" stop-color="#8a1f1a"/>
      <stop offset="0.7" stop-color="#a8603a"/>
      <stop offset="1" stop-color="#3a3a3a"/>
    </linearGradient>
  </defs>

  <!-- Background -->
  <rect class="paper" x="0" y="0" width="858" height="1200"/>
  <path class="field" d="M0,338 C180,320 360,375 540,340 C680,312 790,300 858,272 L858,1200 L0,1200 Z"/>
  <path class="footer-band" d="M0,1152 C300,1150 700,1140 858,1078 L858,1200 L0,1200 Z"/>

  <!-- Brand -->
  <g class="brand">
    <text class="brand-name" x="78" y="218">Tapforge</text>
    <rect class="brand-square" x="532" y="56" width="210" height="210" rx="22"/>
  </g>

  <!-- Device -->
  <rect x="372" y="376" width="204" height="596" rx="30" fill="url(#deviceTone)"
        role="img" aria-label="Smartphone showing a takeaway ordering app with a grid of menu categories"/>

  <!-- Feature ribbons -->
  <g class="features">
    <path class="feature-ribbon" d="M0,450 L232,450 L296,502 L0,502 Z"/>
    <text class="feature-label" x="46" y="494">Ordering</text>

    <path class="feature-ribbon" d="M0,524 L320,524 L372,618 L0,618 Z"/>
    <text class="feature-label" x="37" y="567">Booking And</text>
    <text class="feature-label" x="37" y="611">Reservations</text>

    <path class="feature-ribbon" d="M0,636 L192,636 L296,732 L0,732 Z"/>
    <text class="feature-label" x="37" y="680">Loyalty</text>
    <text class="feature-label" x="37" y="724">program</text>

    <path class="feature-ribbon" d="M0,758 L264,758 L368,854 L0,854 Z"/>
    <text class="feature-label" x="37" y="802">Push</text>
    <text class="feature-label" x="37" y="846">notifications</text>

    <path class="feature-ribbon" d="M0,872 L208,872 L308,970 L0,970 Z"/>
    <text class="feature-label" x="37" y="916">SMART</text>
    <text class="feature-label" x="37" y="962">surveys</text>
  </g>

  <!-- Callouts -->
  <g class="callouts">
    <path class="callout" d="M154,284 H350 Q364,284 364,298 V382 Q364,396 350,396 H200 L188,424 L180,396 H154 Q140,396 140,382 V298 Q140,284 154,284 Z"/>
    <text class="callout-text" x="152" y="312">No more holding</text>
    <text class="callout-text" x="152" y="337">or busy signal</text>
    <text class="callout-text" x="152" y="362">when trying to</text>
    <text class="callout-text" x="152" y="387">place an order.</text>

    <path class="callout" d="M596,328 H758 Q772,328 772,342 V476 Q772,490 758,490 H644 L632,518 L624,490 H596 Q582,490 582,476 V342 Q582,328 596,328 Z"/>
    <text class="callout-text" x="594" y="354">Free-up your</text>
    <text class="callout-text" x="594" y="379">business phone</text>
    <text class="callout-text" x="594" y="404">line at peak</text>
    <text class="callout-text" x="594" y="429">periods, never</text>
    <text class="callout-text" x="594" y="454">miss another</text>
    <text class="callout-text" x="594" y="479">order.</text>

    <path class="callout" d="M620,530 H816 Q830,530 830,544 V628 Q830,642 816,642 H664 L652,670 L644,642 H620 Q606,642 606,628 V544 Q606,530 620,530 Z"/>
    <text class="callout-text" x="618" y="558">No more holding</text>
    <text class="callout-text" x="618" y="583">or busy signal</text>
    <text class="callout-text" x="618" y="608">when trying to</text>
    <text class="callout-text" x="618" y="633">place an order.</text>

    <path class="callout" d="M630,680 H828 Q842,680 842,694 V778 Q842,792 828,792 H676 L664,820 L656,792 H630 Q616,792 616,778 V694 Q616,680 630,680 Z"/>
    <text class="callout-text" x="630" y="707">No more holding</text>
    <text class="callout-text" x="630" y="732">or busy signal</text>
    <text class="callout-text" x="630" y="757">when trying to</text>
    <text class="callout-text" x="630" y="782">place an order.</text>

    <path class="callout" d="M598,834 H760 Q774,834 774,848 V983 Q774,997 760,997 H644 L632,1025 L624,997 H598 Q584,997 584,983 V848 Q584,834 598,834 Z"/>
    <text class="callout-text" x="598" y="860">Free-up your</text>
    <text class="callout-text" x="598" y="885">business phone</text>
    <text class="callout-text" x="598" y="910">line at peak</text>
    <text class="callout-text" x="598" y="935">periods, never</text>
    <text class="callout-text" x="598" y="960">miss another</text>
    <text class="callout-text" x="598" y="985">order.</text>
  </g>

  <!-- Call to action -->
  <g class="cta">
    <path class="cta-fold" d="M32,1088 L132,1144 L112,1088 Z"/>
    <rect class="cta-tab" x="32" y="1036" width="350" height="52"/>
    <path class="cta-url-bar" d="M380,1036 L776,1036 L840,1088 L380,1088 Z"/>
    <text class="cta-text" x="60" y="1078" textLength="302" lengthAdjust="spacingAndGlyphs">ASK FO MORE!</text>
    <text class="cta-url" x="396" y="1076" textLength="392" lengthAdjust="spacingAndGlyphs">www.tapforge-demo.net</text>
  </g>
</svg>
</body>
</html>
```